Business card design needed

We need something on the back that allows the customer to get five stamps then the sixth visit they get 25 dollars to spend.
Business
Quality meat,value for money,spit roast hire, wholesale pubs clubs,cater for bbqs.kessel lane butchery 58 kessel lane.64390217.

```html
<!DOCTYPE html>
<html lang="en">
<head>
<meta charset="utf-8">
<title>Kessel Lane Butchery – Business Card</title>
<link href="https://fonts.googleapis.com/css2?family=Oswald:wght@700&family=PT+Sans:ital,wght@0,400;1,400&family=Open+Sans:ital,wght@1,800&display=swap" rel="stylesheet">
<style>
  :root {
    --brand-red: #b3172b;
    --deep-red: #8e1020;
    --ink: #1c1c1c;
    --paper: #ffffff;
    --backdrop: #d9d9d9;
    --meat-light: #e8a3a0;
    --meat-mid: #c9525a;
    --meat-dark: #9e2a33;
  }
  * { box-sizing: border-box; margin: 0; padding: 0; }
  html, body { width: 1200px; height: 848px; overflow: hidden; }
  body {
    background: var(--backdrop);
    display: flex;
    align-items: center;
    justify-content: center;
    gap: 40px;
  }
  .card {
    width: 540px;
    height: 330px;
    background: var(--paper);
    position: relative;
    overflow: hidden;
    box-shadow: 0 2px 8px rgba(0,0,0,0.15);
  }

  /* Front */
  .card-front { display: flex; flex-direction: column; }
  .business-name {
    font-family: "Oswald", "Arial Narrow", sans-serif;
    font-weight: 700;
    font-size: 46px;
    line-height: 1;
    letter-spacing: -0.5px;
    color: var(--brand-red);
    text-transform: uppercase;
    text-align: center;
    padding-top: 18px;
  }
  .services {
    font-family: "PT Sans", "Helvetica", sans-serif;
    font-style: italic;
    font-size: 19px;
    line-height: 1.2;
    color: var(--ink);
    padding: 6px 0 0 36px;
  }
  .meat-photo {
    flex: 1;
    margin-top: 6px;
    background:
      radial-gradient(ellipse at 30% 60%, var(--meat-mid) 0%, transparent 55%),
      radial-gradient(ellipse at 75% 55%, var(--meat-dark) 0%, transparent 50%),
      linear-gradient(180deg, var(--paper) 0%, var(--meat-light) 35%, var(--meat-mid) 100%);
  }
  .address-band {
    height: 56px;
    background: var(--brand-red);
    color: var(--paper);
    font-family: "PT Sans", "Helvetica", sans-serif;
    font-size: 21px;
    display: flex;
    align-items: center;
    padding-left: 18px;
  }
  .address-band .phone { font-weight: 700; margin-left: 6px; }

  /* Back */
  .card-back { padding: 26px 30px; }
  .loyalty-note {
    font-family: "Open Sans", "Arial", sans-serif;
    font-style: italic;
    font-weight: 800;
    font-size: 20px;
    line-height: 1.25;
    color: var(--ink);
    text-align: center;
  }
  .stamp-grid {
    display: grid;
    grid-template-columns: repeat(3, 90px);
    column-gap: 62px;
    row-gap: 22px;
    justify-content: center;
    margin-top: 22px;
  }
  .stamp {
    width: 84px;
    height: 84px;
    border: 2px solid var(--ink);
    border-radius: 50%;
    display: flex;
    align-items: center;
    justify-content: center;
    font-family: "Open Sans", "Arial", sans-serif;
    font-weight: 800;
    font-style: italic;
    font-size: 34px;
    color: var(--brand-red);
  }
  .reward { position: relative; width: 96px; height: 96px; margin-top: -6px; }
  .reward svg { position: absolute; inset: 0; }
  .reward-text {
    position: absolute; inset: 0;
    display: flex; flex-direction: column;
    align-items: center; justify-content: center;
    font-family: "Open Sans", "Arial", sans-serif;
    font-weight: 800; font-style: italic;
    font-size: 19px; line-height: 1.05;
    color: var(--brand-red);
    transform: rotate(-12deg);
  }
</style>
</head>
<body>

<section class="card card-front">
  <h1 class="business-name">Kessel Lane Butchery</h1>
  <p class="services">Quality meat • Value for money • Spit roast hire<br>• Wholesale pubs clubs • Cater for bbqs</p>
  <div class="meat-photo" role="img" aria-label="Photograph of fresh cuts of raw red meat with a sprig of rosemary and sliced leek"></div>
  <div class="address-band">58 Kessel Lane, North Carrow NSW • <span class="phone">(02) 6439 0217</span></div>
</section>

<section class="card card-back">
  <p class="loyalty-note">Receive a stamp and get $25 off<br>on your 6th visit!</p>
  <div class="stamp-grid">
    <div class="stamp">1</div>
    <div class="stamp">2</div>
    <div class="stamp">3</div>
    <div class="stamp">4</div>
    <div class="stamp">5</div>
    <div class="reward">
      <svg viewBox="0 0 100 100" width="96" height="96" aria-hidden="true">
        <polygon fill="#ffffff" stroke="#b3172b" stroke-width="2.5"
          points="98,50 91.2,58.2 94.4,68.4 84.9,73.4 83.9,83.9 73.4,84.9 68.4,94.4 58.2,91.2 50,98 41.8,91.2 31.6,94.4 26.6,84.9 16.1,83.9 15.1,73.4 5.6,68.4 8.8,58.2 2,50 8.8,41.8 5.6,31.6 15.1,26.6 16.1,16.1 26.6,15.1 31.6,5.6 41.8,8.8 50,2 58.2,8.8 68.4,5.6 73.4,15.1 83.9,16.1 84.9,26.6 94.4,31.6 91.2,41.8"/>
        <circle cx="50" cy="50" r="37" fill="none" stroke="#b3172b" stroke-width="1.5"/>
      </svg>
      <div class="reward-text"><span>$25</span><span>OFF!!</span></div>
    </div>
  </div>
</section>

</body>
</html>
```